BrindleYards.com website homepage re-design

Introduction

Over the last few months, we have dealt with what we would consider B-level website designers. Either they are not up to date with current design techniques, are lazy, or don’t speak English well enough to complete the job. We like to think that we are patient, but this time we are looking (and paying for) top notch service.

Here is a link to the last project that is failing - not because it doesn't have potential, but because the design team really just can't get it together. (also, the front page is just too busy)

http://www.korvanworks.example/project/brindleyards/

We want a new website that lives up to our name as the best professional poker staking company (to understand what we do, look at the current website) in the world and catches the eye of any potential customers/clients.

We need a bright mind that is going to be creative and help us build a powerful website that will stand out among our competitors. We want to be hands-on and give feedback as often as we can.

*****We understand that this project is only for the front page of the site******

What We Do Not Want

Below are website designers that have NOT lived up to our expectations. Please review their portfolios. If you are similar to them in skill, please do not bid. Sorry if this sounds harsh.

http://www.plimtuft-studio.example/
www.korvanz.example
http://www.craftmoleno.example/

**The graphic images and logo were designed by a third party. We think they are good, although might not really “fit” on the website as is shown now.

I uploaded a Zip file with all the source files here: http://www.fileburrow.example/?d=9T2KWQLM

A few good websites we like

http://www.velgrove.example.au/
http://www.quillaby.example.au/

Front Page

Current: http://brindleyards.example/

What we want is a clear, strong, direct message displayed through an animated Flash introduction which really gets our ethos across (see examples below);

We provide staking, free coaching, housing, top notch support and makeup free reward trips to live events which is a massive selling point to those players who are taking poker seriously, so much so that it could and should, along with the amazing coaching we provide, entice players to join even if they don't really need staking. No other site provides this as far as we know and should be a big part of the attraction to our site.

Obviously, the exact details of what we do will need to be explained via ZIP or the phone.

We are the best at what we do and we need to convey that in an impressive way. We offer free coaching, amazing free trips, a forum, a great team environment.

Right now, we have too much going on with the front page, and it needs to be turned into secondary pages

A few websites we like that have strong front page messages are.

***We also have a logo design contest up.

• Flash

```html
<!DOCTYPE html>
<html lang="en">
<head>
<meta charset="utf-8">
<title>BrindleYards – Professional Poker Staking</title>
<link href="https://fonts.googleapis.com/css2?family=Open+Sans:wght@400;600;700&family=Yanone+Kaffeesatz:wght@400;500;600&display=swap" rel="stylesheet">
<style>
:root{
  --ink:#000;
  --panel:#0b1114;
  --panel-edge:#1c2a30;
  --header-top:#0a2230;
  --header-bottom:#04131c;
  --nav-top:#d6f0fb;
  --nav-bottom:#6cc2e6;
  --nav-text:#0b2d44;
  --cyan:#2fc1ee;
  --sky:#5ab8e8;
  --lime:#9bf02a;
  --green:#3fd44a;
  --yellow:#f5e617;
  --orange:#ff9a2a;
  --amber:#f6b12d;
  --tan:#b9aa88;
  --body:#8fc7dd;
  --text:#e7eef2;
  --muted:#b9c4c9;
  --button-dark:#0c5b93;
}
*{box-sizing:border-box;margin:0;padding:0}
html,body{width:771px;height:1200px;overflow:hidden;background:var(--ink)}
body{position:relative;font-family:"Open Sans",Arial,sans-serif;color:var(--text)}
.abs{position:absolute}
a{color:inherit;text-decoration:none}

/* header */
.site-header{left:0;top:0;width:771px;height:125px;background:linear-gradient(var(--header-top),var(--header-bottom))}
.brand{left:40px;top:36px;display:flex;align-items:center;gap:14px}
.brand-mark{width:58px;height:58px;border-radius:50%;background:#1e8fe0}
.brand-name{font-size:34px;font-weight:700;color:#fff;letter-spacing:1px;line-height:1}
.brand-tag{left:146px;top:93px;font-size:8px;font-weight:700;color:#fff;letter-spacing:.5px}
.apply-btn{left:600px;top:16px;width:156px;height:29px;border-radius:5px;background:linear-gradient(#d6ff5a,#7fe21a);color:#0a2a10;font-weight:700;font-size:17px;letter-spacing:1px;display:flex;align-items:center;justify-content:center;gap:10px;box-shadow:0 0 6px #8cf03a}
.call-label{left:697px;top:60px;font-family:"Yanone Kaffeesatz",sans-serif;font-size:19px;color:var(--sky)}
.call-number{left:648px;top:85px;font-size:16px;font-weight:700;color:var(--yellow)}

/* navigation */
.main-nav{left:0;top:126px;width:771px;height:30px;background:linear-gradient(var(--nav-top),var(--nav-bottom));display:flex;align-items:center;padding-left:10px}
.main-nav a{font-size:11px;color:var(--nav-text);padding:0 11px;border-right:1px solid #8bc3da;line-height:14px}
.main-nav a:last-child{border-right:0}
.search{left:589px;top:133px;width:170px;height:17px;background:#fff;border:1px solid #4f9cc4;border-radius:8px 0 0 8px;font-size:8px;color:#777;padding:3px 8px}
.search-btn{left:736px;top:133px;width:24px;height:17px;background:#1f80c4;border-radius:0 5px 5px 0}

/* hero slider */
.hero{left:15px;top:180px;width:747px;height:285px;border:7px solid var(--tan);background:linear-gradient(180deg,#061a26 0%,#0a3550 50%,#05121a 100%);overflow:hidden}
.hero-welcome{left:31px;top:84px;font-family:"Yanone Kaffeesatz",sans-serif;font-size:22px;color:var(--cyan)}
.hero-name{left:31px;top:110px;font-size:28px;font-weight:700;color:#fff;letter-spacing:1px;line-height:1}
.hero-tag{left:31px;top:147px;font-size:19px;font-weight:700;color:var(--lime)}
.hero-tag span{color:var(--cyan)}
.hero-art{left:330px;top:0;width:403px;height:246px;background:radial-gradient(ellipse 45% 55% at 60% 50%,#4aa8f2 0%,#2474d0 35%,rgba(14,70,120,.6) 60%,rgba(10,53,80,0) 80%)}
.hero-bar{left:0;top:246px;width:733px;height:25px;background:#04121a}
.hero-dots{left:12px;top:255px;display:flex;gap:6px}
.hero-dots i{width:8px;height:8px;border-radius:50%;background:#9aa4a8}
.hero-controls{left:648px;top:253px}

/* welcome */
.welcome{left:15px;top:478px;width:747px;height:183px;background:var(--panel);border:1px solid var(--panel-edge)}
.welcome-title{left:12px;top:6px;font-family:"Yanone Kaffeesatz",sans-serif;font-weight:400;font-size:21px;color:var(--green)}
.welcome-title b{color:var(--cyan);font-weight:500}
.welcome-rule{left:12px;top:36px;width:400px;height:1px;background:#233840}
.welcome-copy{left:13px;top:48px;width:405px;font-size:7.8px;line-height:11px;color:var(--body)}
.welcome-copy p+p{margin-top:11px}
.read-more{font-size:8.3px;color:var(--lime)}
.read-more::before{content:"» ";color:#cfd8da}
.testimonial{left:464px;top:9px;width:272px;height:112px;border-radius:14px;background:linear-gradient(#3aa6e6,#1175c4);padding:5px 14px}
.testimonial h3{font-family:"Yanone Kaffeesatz",sans-serif;font-weight:400;font-size:21px;color:#062a44;border-bottom:1px solid #7fc7ee;padding-bottom:2px}
.testimonial p{font-size:7.6px;line-height:10px;color:#fff;margin-top:5px}
.testimonial-tail{left:484px;top:120px}
.testimonial-by{left:478px;top:141px;font-size:9px;font-weight:700;color:var(--cyan)}
.testimonial-by span{color:var(--lime)}
.more-testimonials{left:592px;top:138px;width:140px;height:18px;background:linear-gradient(#ffd36a,var(--amber));font-size:8.3px;font-weight:700;color:#231400;display:flex;align-items:center;justify-content:center}

/* features */
.feature{top:680px;width:182px}
.feature h2{font-family:"Yanone Kaffeesatz",sans-serif;font-weight:500;font-size:18px;line-height:18px}
.feature .thumb{margin-top:11px;width:181px;height:70px;border:1px solid}
.feature p{margin-top:12px;font-size:7.8px;line-height:11px;color:var(--muted);height:55px;overflow:hidden}
.feature .read-more{display:block;margin:8px 0 0 4px}
.f-staking h2{color:var(--cyan)}
.f-staking .thumb{border-color:var(--cyan);background:radial-gradient(ellipse at 35% 55%,#4aa4f0 0%,#1c68c0 40%,#0a2238 85%)}
.f-strategy h2{color:var(--green)}
.f-strategy .thumb{border-color:var(--green);background:radial-gradient(ellipse at 50% 60%,#d9dcd8 0%,#5a6a60 22%,#1a6a32 45%,#0f4a22 90%)}
.f-forums h2{color:var(--orange)}
.f-forums .thumb{border-color:#c98a40;background:linear-gradient(#e6dccd 0%,#b8a690 40%,#4a3c30 62%,#a6896a 100%)}
.f-radio h2{color:var(--cyan)}
.f-radio .thumb{border-color:#6b4a3a;background:radial-gradient(ellipse at 30% 50%,#e8dcc4 0%,#9a8270 30%,#3a221c 60%),linear-gradient(#3a221c,#3a221c)}

/* lower section */
.lower{left:0;top:877px;width:771px;height:265px;background:#050a0c}
.news h2,.blog h2{font-family:"Yanone Kaffeesatz",sans-serif;font-weight:500;font-size:18px;line-height:20px}
.news{left:22px;top:899px;width:220px}
.news h2{color:var(--cyan)}
.news-list{margin-top:10px;padding-left:5px;font-size:8px;line-height:11px}
.news-list .head{color:var(--amber);font-weight:700}
.news-list .date{color:var(--muted)}
.news-list .date.hot{color:var(--amber);font-weight:700}
.news-list p{color:var(--muted)}
.news-list .gap{height:12px}
.btn-more{height:15px;background:linear-gradient(#2c9ae0,var(--button-dark));font-size:8.3px;font-weight:700;color:#fff;display:flex;align-items:center;justify-content:center}
.blog{left:272px;top:899px;width:280px}
.blog h2{color:var(--green)}
.blog-entry{position:absolute;left:0;width:280px;height:45px}
.blog-thumb{position:absolute;left:0;top:0;width:49px;height:42px;border:1px solid #555;background:linear-gradient(#d9c2ae,#8a6e5c)}
.blog-entry h4{position:absolute;left:58px;top:-1px;font-size:8.5px;font-weight:700;color:var(--cyan)}
.blog-entry p{position:absolute;left:58px;top:12px;width:220px;font-size:7.8px;line-height:11px;color:#fff;text-decoration:underline}
.sidebar{left:567px;top:926px;width:187px;height:194px;background:#0e1a1d}
.converter-banner{left:572px;top:931px;width:176px;height:36px;background:linear-gradient(#0a2a50,#124a80)}
.converter-art{left:572px;top:968px;width:176px;height:58px;background:linear-gradient(90deg,#2a3a34,#c8b8b8 60%,#e8d8d8)}
.subscribe-title{left:572px;top:1033px;font-family:"Yanone Kaffeesatz",sans-serif;font-size:17px;color:var(--cyan)}
.sub-input{left:574px;width:130px;height:12px;background:#fff;font-size:8px;color:#333;padding:0 5px;line-height:12px}
.sub-btn{left:574px;top:1098px;width:73px;height:14px}

/* footer */
.site-footer{left:0;top:1148px;width:771px;height:52px;background:#000}
.footer-links{left:0;top:1167px;width:771px;text-align:center;font-size:8.3px;color:#e8e8e8}
.footer-links span{margin:0 9px;color:#aaa}
.copyright{left:0;top:1186px;width:771px;text-align:center;font-size:8.3px;color:#e8e8e8}
</style>
</head>
<body>

<header class="site-header abs">
  <div class="brand abs"><span class="brand-mark"></span><span class="brand-name">BrindleYards</span></div>
  <div class="brand-tag abs">PROFESSIONAL POKER STAKING</div>
  <a class="apply-btn abs" href="#">APPLY NOW <span>»»</span></a>
  <div class="call-label abs">CALL US</div>
  <div class="call-number abs">555.0142.0199</div>
</header>

<nav class="main-nav abs">
  <a href="#">Home</a><a href="#">Management Team</a><a href="#">Coaching</a><a href="#">FAQs</a><a href="#">Forums</a><a href="#">Blog</a><a href="#">Apply</a><a href="#">Contact</a>
</nav>
<div class="search abs">Search</div>
<div class="search-btn abs">
  <svg width="24" height="17" viewBox="0 0 24 17"><circle cx="11" cy="7.5" r="3.5" fill="none" stroke="#fff" stroke-width="1.5"/><line x1="13.5" y1="10" x2="16" y2="12.5" stroke="#fff" stroke-width="1.8"/></svg>
</div>

<section class="hero abs">
  <div class="hero-art abs" role="img" aria-label="Stack of blue poker chips shaped like a stable with flying chips"></div>
  <div class="hero-welcome abs">Welcome to</div>
  <div class="hero-name abs">BrindleYards</div>
  <div class="hero-tag abs">PROFESSIONAL <span>POKER STAKING</span></div>
  <div class="hero-bar abs"></div>
  <div class="hero-dots abs"><i></i><i></i><i></i><i></i><i></i></div>
  <svg class="hero-controls abs" width="60" height="12" viewBox="0 0 60 12">
    <rect x="0" y="1" width="2" height="10" fill="#fff"/><polygon points="10,1 3,6 10,11" fill="#fff"/>
    <rect x="24" y="1" width="3" height="10" fill="#fff"/><rect x="29" y="1" width="3" height="10" fill="#fff"/>
    <polygon points="44,1 51,6 44,11" fill="#fff"/><rect x="52" y="1" width="2" height="10" fill="#fff"/>
  </svg>
</section>

<section class="welcome abs">
  <h1 class="welcome-title abs">welcome to <b>BRINDLEYARDS</b></h1>
  <div class="welcome-rule abs"></div>
  <div class="welcome-copy abs">
    <p>Our mission is to invest in the best online poker players, build a professional and personal relationship with them, and profit together as a team. We stake players in low-stakes cash games to high-stakes multi-table tournaments and everything in between.</p>
    <p>Online Poker Staking is our livelihood, our focus, and our number one priority. The result is better client relations, faster feedback, smooth and flexible staking deals, and solid results. We take an active interest in our players and devise creative, flexible arrangements to accommodate a wide array of staking needs. Click here to read what some of our players have to say about their experience with BrindleYards!</p>
    <p style="margin-top:12px"><a class="read-more" href="#">read more</a></p>
  </div>
  <div class="testimonial abs">
    <h3>Testimonials</h3>
    <p>Morven's vast knowledge and laid back coaching style makes every session a great learning experience! Morven takes an active role in his student's poker development, he is always available to answer questions and offer advice. He has helped me go from a break even, swingy player to a consistent 3 to 4 bb/100. His relationship with his students is more of a mentor/friend than a teacher/pupil.</p>
  </div>
  <svg class="testimonial-tail abs" width="70" height="18" viewBox="0 0 70 18"><polygon points="20,0 70,0 0,18" fill="#1175c4"/></svg>
  <div class="testimonial-by abs">Tavish - <span>New York</span></div>
  <a class="more-testimonials abs" href="#">Read More Testimonials &nbsp;»</a>
</section>

<article class="feature f-staking abs" style="left:16px">
  <h2>Staking</h2>
  <div class="thumb" role="img" aria-label="Blue poker chip stable with chips"></div>
  <p>Staking is the core of our business. We began BrindleYards with the goal of being the most player friendly backers in the world, and we continue to strive to meet those lofty expectations.</p>
  <a class="read-more" href="#">read more</a>
</article>
<article class="feature f-strategy abs" style="left:204px">
  <h2>Strategy</h2>
  <div class="thumb" role="img" aria-label="Joker card, poker chip and dice on green felt"></div>
  <p>The newly launched Brindle Strateg offers a great opportunity to improve your poker game. Watch videos and listen to commentary from some of the best poker players in the world.</p>
  <a class="read-more" href="#">read more</a>
</article>
<article class="feature f-forums abs" style="left:392px">
  <h2>Forums</h2>
  <div class="thumb" role="img" aria-label="Circle of chairs in a meeting room"></div>
  <p>The Brindle Forums have quickly become the place to discuss poker strategy. The forum is bubbling with poker commentary and questions. Forum members include high-stakes Brindle team members, low-stakes Brindle team members .....</p>
  <a class="read-more" href="#">read more</a>
</article>
<article class="feature f-radio abs" style="left:580px">
  <h2>Poker Radio</h2>
  <div class="thumb" role="img" aria-label="Lucky playing card banner next to a blue microphone"></div>
  <p>Lorem ipsum dolor sit amet, consectetur adipiscing elit. Maecenas quis lacus enim. Mauris enim neque, sagittis vel sagittis a, venenatis ut metus. Donec ultrices, augue eu pulvinar iaculis, lorem sem ultrices risus, et</p>
  <a class="read-more" href="#">read more</a>
</article>

<section class="lower abs"></section>

<section class="news abs">
  <h2>Recent News</h2>
  <div class="news-list">
    <div class="head">Harrow Players forums are now OPEN!</div>
    <div class="date">2010-12-08</div>
    <div class="gap"></div>
    <p>Corwin's forums are now open to all his students. Be sure to catch the recent Tip Of The Week!</p>
    <div class="head">VEGAS BABY, YEAH!</div>
    <div class="date hot">2010-12-08</div>
    <div class="gap"></div>
    <p>It's official! We now have our very own house in vegas. Check out Ellard's thread for details &amp; pics or...</p>
    <div class="head">Tweeting Tweets on Chirpline!</div>
    <div class="date hot">2010-12-08</div>
  </div>
  <a class="btn-more" href="#" style="width:87px;margin:13px 0 0 5px">More News &nbsp;»</a>
</section>

<section class="blog abs">
  <h2>Blog</h2>
  <div class="blog-entry" style="top:33px">
    <div class="blog-thumb" role="img" aria-label="Blog author portrait"></div>
    <h4>Mr Ned Quillfarrow</h4>
    <p>Lorem ipsum dolor sit amet, consectetur adipiscing elit. Maecenas quis lacus enim. Mauris enim neque, sagittis vel sagittis a, venenatis ut metus.</p>
  </div>
  <div class="blog-entry" style="top:89px">
    <div class="blog-thumb" role="img" aria-label="Blog author portrait"></div>
    <h4>Mr Ned Quillfarrow</h4>
    <p>Lorem ipsum dolor sit amet, consectetur adipiscing elit. Maecenas quis lacus enim. Mauris enim neque, sagittis vel sagittis a, venenatis ut metus.</p>
  </div>
  <div class="blog-entry" style="top:145px">
    <div class="blog-thumb" role="img" aria-label="Blog author portrait"></div>
    <h4>Mr Ned Quillfarrow</h4>
    <p>Lorem ipsum dolor sit amet, consectetur adipiscing elit. Maecenas quis lacus enim. Mauris enim neque, sagittis vel sagittis a, venenatis ut metus.</p>
  </div>
  <a class="btn-more abs" href="#" style="left:59px;top:202px;width:102px">More Blog Entry &nbsp;»</a>
</section>

<aside class="sidebar abs"></aside>
<div class="converter-banner abs" role="img" aria-label="Hand history converter lettering, coming soon"></div>
<div class="converter-art abs" role="img" aria-label="Playing cards and chips on a table"></div>
<div class="subscribe-title abs">Subscribe Newsletter</div>
<div class="sub-input abs" style="top:1058px">your email id</div>
<div class="sub-input abs" style="top:1077px">your email id</div>
<a class="btn-more sub-btn abs" href="#">Subscribe &nbsp;»</a>

<footer class="site-footer abs"></footer>
<div class="footer-links abs">Home<span>|</span>Management Team<span>|</span>Coaching<span>|</span>FAQs<span>|</span>Forums<span>|</span>Blog<span>|</span>Apply<span>|</span>Contact</div>
<div class="copyright abs">©2011 Copyright, brindleyards.com &nbsp; | &nbsp; All Rights Reserved</div>

</body>
</html>
```